App UI Design: Shopping/E-commerce App

Project :
Develop an UI design & App icon for an E-commerce/Shopping App

About the App/ Target Audience:
This grocery & food shopping app will be used by independent pub, café, restaurant owners to place & manage their purchases of foods and groceries for their catering businesses.

They will use the app to access product catalogues & special promotions, search & buy large quantities of groceries or catering supplies, and the ability to manage and track status of their order.

The HTML5 App’s has been built with a very basic structure. It now needs the visual layer of the UI designed

Note:
The app is tailored for business & catering orders, not retail/supermarket buyers, so the visual needs to look smart & not too casual.
Updates

Reason: Current submissions have not met out expectations. Please use the similar app examples in the PDF as a strong point of reference for the look & feel. Feedback will be given as submissions come in, please feel free to submit initial concepts of 1 or 2 of the pages & we'll provide feedback on whether it is on the right track or not before you do more work. Current submission will also receive feedback in the next few days. We look forward to new submissions!

Target Market(s)

Male & Female. Independent pub, café, restaurant owners buying for their catering businesses. Chefs etc.

Industry/Entity Type

Restaurant

Requirements
Must have
• An overview of elements/pages of the app that needs to be designed are:
(DOWNLOAD a more detailed diagram PDF explanation)

1. Welcome- Log-in Page
2. Homepage – index that links to different function of the app

Products:
3. Promotions page – for products on special for a limited time
4. Catalogue page – access to a range of catalogue

Ways to buy:
5. Basket (Shopping Cart) - tracking items they are buying from the catalogues
6. Templates (Pre-set Shopping list)- Set shopping list that has been preloaded for certain menu
7. Open Order page

My Account:
8. My Account/profile page – Users can check the status of their order, look at past orders, look at their account number & details etc

_______________________________________________________

Icon set- Icons to represent each pages that act as visual cues for easier browsing.

2 Main features that need to be accessible & consistent throughout all pages are:
a) The Navigation Bar –
so the user can quickly find their way back & access to the main functions
b) The Search bar –
whether it drops down when needed, or is featured as a header/footer.
c) Log out button
Nice to have

Things to keep in mind:

The UI design essentially needs to be a customizable template that can easily adapt to any brand/logo with a slight change of the color scheme. As we will later implement our brand & logo onto it.

We’re looking for a clean & clear design that allows for a straight forward easy user experience.

You are free to develop different layout & UI pattern that you feel is the most efficient way the user can walk through the App & make their purchase in no more than 2 or 3 clicks
________________________________________________

Screenshot of Similar Apps for reference are also in the PDF

```html
<!DOCTYPE html>
<html lang="en">
<head>
<meta charset="utf-8">
<title>Chef's Pantry – Home</title>
<link href="https://fonts.googleapis.com/css2?family=Roboto+Condensed:wght@400;700&family=Arimo:wght@400&display=swap" rel="stylesheet">
<style>
  :root{
    --page-bg:#ededed;
    --bar-top:#4f82cc;
    --bar-bottom:#3565ad;
    --nav-top:#3a6ab2;
    --nav-bottom:#2d5a9e;
    --divider-dark:#244b86;
    --divider-light:#5b89cc;
    --hero-center:#4676bd;
    --hero-edge:#23487f;
    --accent-yellow:#f5cf12;
    --text-light:#ffffff;
    --text-soft:#d6e3f5;
    --tile-top:#fbfbfb;
    --tile-bottom:#e2e2e2;
    --tile-border:#c9c9c9;
    --tile-text:#3a3a3a;
    --search-top:#ffffff;
    --search-bottom:#dedede;
    --empty:#f0f0f0;
  }
  *{box-sizing:border-box;margin:0;padding:0}
  html,body{width:1013px;height:1200px;overflow:hidden;background:var(--page-bg)}
  .app{position:absolute;left:106px;top:0;width:801px;height:1200px;display:flex;flex-direction:column;background:var(--empty);font-family:"Roboto Condensed",sans-serif}
  .top-bar{height:115px;background:linear-gradient(var(--bar-top),var(--bar-bottom));display:flex;align-items:center;justify-content:space-between;padding:0 50px}
  .bar-button{height:44px;display:flex;align-items:center;color:var(--text-light);font-size:17px;font-family:"Arimo",sans-serif}
  .bar-button svg{position:absolute}
  .bar-button span{position:relative;width:100%;text-align:center}
  .back-button,.logout-button{position:relative;width:120px}
  .main-nav{height:82px;background:linear-gradient(var(--nav-top),var(--nav-bottom));display:flex;align-items:center;justify-content:center;border-top:1px solid var(--divider-light);border-bottom:1px solid var(--divider-dark)}
  .main-nav a{color:var(--text-light);text-decoration:none;font-size:17px;padding:0 18px;line-height:50px;border-left:1px solid var(--divider-dark);box-shadow:inset 1px 0 0 var(--divider-light)}
  .main-nav a:first-child{border-left:none;box-shadow:none}
  .hero{height:388px;background:radial-gradient(ellipse 60% 70% at 50% 45%,var(--hero-center),var(--hero-edge));text-align:center;position:relative}
  .brand-name{position:absolute;left:0;right:0;top:78px;font-family:"Roboto Condensed",sans-serif;font-weight:700;font-size:72px;line-height:90px;color:var(--accent-yellow)}
  .hero-intro{position:absolute;left:100px;right:100px;top:206px;font-family:"Arimo",sans-serif;font-size:15px;line-height:19px;color:var(--text-soft)}
  .menu-grid{height:400px;display:grid;grid-template-columns:1fr 1fr;grid-template-rows:repeat(3,1fr)}
  .menu-tile{background:linear-gradient(var(--tile-top),var(--tile-bottom));border-bottom:1px solid var(--tile-border);display:flex;flex-direction:column;align-items:center;justify-content:center;gap:12px;color:var(--tile-text);font-size:32px;text-transform:uppercase;text-decoration:none}
  .menu-tile:nth-child(odd){border-right:2px solid var(--tile-border)}
  .menu-tile svg{width:44px;height:44px;stroke:var(--tile-text);fill:none;stroke-width:2.2}
  .search-bar{height:87px;background:linear-gradient(var(--search-top),var(--search-bottom));display:flex;align-items:center;justify-content:center;border-bottom:1px solid var(--tile-border)}
  .search-field{width:342px;height:32px;border-radius:16px;border:1px solid #c4c4c4;background:#fff;box-shadow:inset 0 2px 3px rgba(0,0,0,.12);display:flex;align-items:center;padding-left:220px;gap:8px;color:#8a8a8a;font-family:"Arimo",sans-serif;font-size:17px}
  .empty-area{flex:1;background:var(--empty)}
</style>
</head>
<body>
<main class="app">
  <header class="top-bar">
    <a class="bar-button back-button">
      <svg width="120" height="44" viewBox="0 0 120 44"><defs><linearGradient id="btn" x1="0" y1="0" x2="0" y2="1"><stop offset="0" stop-color="#5b8fd9"/><stop offset="1" stop-color="#2f5fa8"/></linearGradient></defs><path d="M2 22 L20 2 H116 a3 3 0 0 1 3 3 V39 a3 3 0 0 1 -3 3 H20 Z" fill="url(#btn)" stroke="#244b86" stroke-width="1.5"/></svg>
      <span>Back</span>
    </a>
    <a class="bar-button logout-button">
      <svg width="120" height="44" viewBox="0 0 120 44"><path d="M118 22 L100 2 H4 a3 3 0 0 0 -3 3 V39 a3 3 0 0 0 3 3 H100 Z" fill="url(#btn)" stroke="#244b86" stroke-width="1.5"/></svg>
      <span>Log Out</span>
    </a>
  </header>

  <nav class="main-nav">
    <a>Promotions</a><a>Catalogue</a><a>Basket</a><a>Order Template</a><a>Open Order</a><a>My Account</a>
  </nav>

  <section class="hero">
    <h1 class="brand-name">Chef's Pantry</h1>
    <p class="hero-intro">Lorem ipsum dolor sit amet, in cum iusto sonet nihil.<br>Vel et laudem fierent. Per te duis omnes iuvaret, in nec debet splendide<br>adversarium. Mei ad prompta necessitatibus.</p>
  </section>

  <section class="menu-grid">
    <a class="menu-tile"><svg viewBox="0 0 44 44"><path d="M10 5H34M10 39H34M13 5C13 16 31 18 31 22S13 28 13 39M31 5C31 16 13 18 13 22S31 28 31 39"/></svg>Promotions</a>
    <a class="menu-tile"><svg viewBox="0 0 44 44"><rect x="7" y="7" width="30" height="30" rx="5"/><path d="M7 15H37M13 21H20M24 21H31M13 27H20M24 27H31"/></svg>Catalogue</a>
    <a class="menu-tile"><svg viewBox="0 0 44 44"><path d="M5 10H11L16 28H34L37 16H13"/><circle cx="18" cy="34" r="3"/><circle cx="31" cy="34" r="3"/></svg>Basket</a>
    <a class="menu-tile"><svg viewBox="0 0 44 44"><rect x="8" y="13" width="22" height="26" rx="2"/><path d="M15 13V6H36V32H30"/></svg>Order Template</a>
    <a class="menu-tile"><svg viewBox="0 0 44 44"><rect x="9" y="5" width="26" height="34" rx="4"/><path d="M15 13H24M15 19H22M15 25H21"/><path d="M32 22C28 22 27 26 30 27S33 31 29 32M30 20V34"/></svg>Open Order</a>
    <a class="menu-tile"><svg viewBox="0 0 44 44"><circle cx="22" cy="22" r="6"/><path d="M22 5L25 10L31 8L31 14L37 16L34 22L37 28L31 30L31 36L25 34L22 39L19 34L13 36L13 30L7 28L10 22L7 16L13 14L13 8L19 10Z"/></svg>My Account</a>
  </section>

  <div class="search-bar">
    <label class="search-field">
      <svg width="16" height="16" viewBox="0 0 16 16" fill="none" stroke="#666" stroke-width="2"><circle cx="10" cy="6" r="4.5"/><path d="M6.5 9.5L2 14"/></svg>
      search
    </label>
  </div>

  <div class="empty-area"></div>
</main>
</body>
</html>
```